Rocket business card

Modern business card design, use of color is good with clean space too.

Things to include on card:

Quote: I add fuel to your optometry practice

- Eyewear Sales
- Admin Duties
- Revenue Collection
- Leadership
- Tech Adoption
- COGS Reduction
- Product Sourcing
-Medical Growth

Dalton Vessey, CEO
Glint Harbor
Text Me! 847-302-1964
dalton@glintharbor.example

```html
<!DOCTYPE html>
<html lang="en">
<head>
<meta charset="utf-8">
<title>Glint Harbor — Business Card</title>
<link rel="stylesheet" href="https://fonts.googleapis.com/css2?family=Roboto:wght@400;500;700&display=swap">
<style>
  :root {
    --bg: #e6e6e6;
    --card: #ffffff;
    --ink: #111111;
    --grey: #555555;
    --orange: #f07c1b;
    --orange-deep: #e8501f;
  }
  * { box-sizing: border-box; margin: 0; padding: 0; }
  html, body { width: 1200px; height: 960px; overflow: hidden; }
  body {
    background: var(--bg);
    font-family: "Roboto", Arial, sans-serif;
    position: relative;
  }
  .card {
    position: absolute;
    width: 700px;
    height: 400px;
    background: var(--card);
    overflow: hidden;
    box-shadow: 0 6px 18px rgba(0,0,0,0.18);
  }
  .card--front { left: 90px; top: 50px; }
  .card--back { left: 410px; top: 510px; }
  .card .swoosh { position: absolute; left: 0; top: 0; width: 700px; height: 400px; }

  .brand {
    position: absolute;
    display: flex;
    align-items: center;
    gap: 14px;
    z-index: 1;
  }
  .brand__dot {
    border-radius: 50%;
    background: linear-gradient(135deg, var(--orange), var(--orange-deep));
  }
  .brand__name {
    font-weight: 500;
    color: var(--ink);
    letter-spacing: 0.04em;
    text-transform: uppercase;
    white-space: nowrap;
  }

  .card--front .brand { left: 0; right: 0; top: 160px; justify-content: center; }
  .card--front .brand__dot { width: 62px; height: 62px; }
  .card--front .brand__name { font-size: 40px; }

  .services {
    position: absolute;
    left: 0; right: 0; top: 250px;
    text-align: center;
    color: var(--grey);
    font-size: 17px;
    line-height: 1.35;
  }
  .services .sep { color: var(--orange); margin: 0 6px; }

  .card--back .brand { left: 70px; top: 170px; }
  .card--back .brand__dot { width: 46px; height: 46px; }
  .card--back .brand__name { font-size: 30px; }

  .contact {
    position: absolute;
    left: 410px; top: 92px;
    z-index: 1;
  }
  .contact__name { color: var(--orange); font-weight: 700; font-size: 26px; }
  .contact__role { color: var(--ink); font-weight: 500; font-size: 15px; margin: 2px 0 18px; }
  .contact__list { list-style: none; font-size: 15px; color: var(--grey); }
  .contact__list li { display: flex; align-items: center; gap: 8px; margin-bottom: 4px; }
  .contact__list svg { width: 13px; height: 13px; fill: var(--orange); flex: none; }
</style>
</head>
<body>

<section class="card card--front">
  <svg class="swoosh" viewBox="0 0 700 400" aria-hidden="true">
    <path d="M0 0 H700 V12 C470 26 220 70 0 130 Z" fill="var(--ink)"/>
    <path d="M30 146 C240 84 470 40 700 26" fill="none" stroke="var(--ink)" stroke-width="2"/>
  </svg>
  <div class="brand">
    <span class="brand__dot"></span>
    <span class="brand__name">Glint Harbor</span>
  </div>
  <p class="services">
    Eyewear Sales<span class="sep">•</span>Admin Duties<span class="sep">•</span>Revenue Collection<br>
    Leadership<span class="sep">•</span>Tech Adoption<span class="sep">•</span>COGS Reduction<br>
    Product Sourcing<span class="sep">•</span>Medical Growth
  </p>
</section>

<section class="card card--back">
  <svg class="swoosh" viewBox="0 0 700 400" aria-hidden="true">
    <path d="M700 400 H0 V386 C230 372 480 330 700 280 Z" fill="var(--ink)"/>
    <path d="M700 264 C470 318 230 356 0 370" fill="none" stroke="var(--ink)" stroke-width="2"/>
  </svg>
  <div class="brand">
    <span class="brand__dot"></span>
    <span class="brand__name">Glint Harbor</span>
  </div>
  <div class="contact">
    <p class="contact__name">Dalton Vessey</p>
    <p class="contact__role">CEO</p>
    <ul class="contact__list">
      <li><svg viewBox="0 0 24 24"><path d="M6.6 10.8a15 15 0 0 0 6.6 6.6l2.2-2.2c.3-.3.7-.4 1-.2 1.1.4 2.3.6 3.6.6.6 0 1 .4 1 1V20c0 .6-.4 1-1 1A17 17 0 0 1 3 4c0-.6.4-1 1-1h3.5c.6 0 1 .4 1 1 0 1.3.2 2.5.6 3.6.1.3 0 .7-.2 1z"/></svg>847-302-1964 (Text Me!)</li>
      <li><svg viewBox="0 0 24 24"><path d="M2 5h20v14H2z M2 5l10 8 10-8" /></svg>dalton@glintharbor.example</li>
      <li><svg viewBox="0 0 24 24"><circle cx="12" cy="12" r="10"/></svg>www.glintharbor.example</li>
    </ul>
  </div>
</section>

</body>
</html>
```